Electrician Needs A Business Card

I already have a logo and would like a business card to be designed based around this logo the company is called Tolvane Electrical Pty Ltd

The business card will be printed on transparent plastic so I need it to stand out from the crowd. I do not want the card to have anything to do with Electrical on it eg light bulbs, power points etc

I need it to have the following details.

Gareth Pomfrey
Mobile : 0437 519 284
email : gareth@tolvaneelectrical.com.au

If it could incorporate the following onto the bottom of the card
ELECTRICAL - COMMUNICATIONS - AUDIO - VISUAL

```html
<!DOCTYPE html>
<html lang="en">
<head>
<meta charset="utf-8">
<title>Tolvane Electrical – Business Card</title>
<link rel="stylesheet" href="https://fonts.googleapis.com/css2?family=Arimo:wght@400;700&display=swap">
<style>
  :root {
    --page: #ffffff;
    --card: #ffffff;
    --card-edge: #4a4a4a;
    --ink: #333333;
    --accent: #f7a62b;
    --band: #2b2b2b;
    --band-text: #ffffff;
  }
  * { box-sizing: border-box; margin: 0; padding: 0; }
  html, body {
    width: 1200px;
    height: 1000px;
    overflow: hidden;
    background: var(--page);
    font-family: "Arimo", Arial, sans-serif;
  }
  .business-card {
    position: absolute;
    left: 80px;
    top: 157px;
    width: 1040px;
    height: 686px;
    background: var(--card);
    border: 1.5px solid var(--card-edge);
    overflow: hidden;
  }
  .brand {
    position: absolute;
    right: 62px;
    top: 62px;
    display: flex;
    align-items: center;
    gap: 30px;
  }
  .brand-name {
    font-size: 62px;
    line-height: 58px;
    font-weight: 400;
    color: var(--ink);
    text-align: left;
  }
  .brand-mark {
    width: 150px;
    height: 150px;
    background: var(--accent);
  }
  .holder-name {
    position: absolute;
    left: 66px;
    top: 372px;
    font-size: 35px;
    font-weight: 700;
    letter-spacing: 2.5px;
    color: var(--ink);
  }
  .divider {
    position: absolute;
    left: 0;
    top: 419px;
    width: 100%;
    height: 13px;
    background: var(--accent);
  }
  .contact-list {
    position: absolute;
    left: 22px;
    top: 448px;
    list-style: none;
  }
  .contact-item {
    display: flex;
    align-items: center;
    height: 38px;
    font-size: 27px;
    color: var(--ink);
  }
  .contact-icon {
    width: 30px;
    height: 30px;
    margin-right: 14px;
    flex: none;
  }
  .services-band {
    position: absolute;
    left: 0;
    bottom: 0;
    width: 100%;
    height: 112px;
    background: var(--band);
    display: flex;
    justify-content: center;
    padding-top: 20px;
    font-size: 36px;
    color: var(--band-text);
    white-space: pre;
  }
  .service-highlight { color: var(--accent); }
</style>
</head>
<body>
  <div class="business-card">
    <div class="brand">
      <div class="brand-name">Tolvane<br>Electrical</div>
      <div class="brand-mark"></div>
    </div>

    <div class="holder-name">Gareth Pomfrey</div>
    <div class="divider"></div>

    <ul class="contact-list">
      <li class="contact-item">
        <svg class="contact-icon" viewBox="0 0 30 30" aria-hidden="true">
          <path d="M9 3 h5 v6 h-3 c-1 4 -1 8 0 12 h3 v6 h-5 c-4 -7 -4 -17 0 -24 z" fill="var(--accent)"/>
        </svg>
        0437 519 284
      </li>
      <li class="contact-item">
        <svg class="contact-icon" viewBox="0 0 30 30" aria-hidden="true">
          <g fill="none" stroke="var(--accent)" stroke-width="1.6">
            <circle cx="15" cy="15" r="11"/>
            <ellipse cx="15" cy="15" rx="5" ry="11"/>
            <line x1="4" y1="15" x2="26" y2="15"/>
            <line x1="15" y1="4" x2="15" y2="26"/>
            <path d="M6 9 h18 M6 21 h18"/>
          </g>
        </svg>
        gareth@tolvaneelectrical.com.au
      </li>
    </ul>

    <div class="services-band"><span class="service-highlight">ELECTRICAL</span> - COMMUNICATIONS - <span class="service-highlight">AUDIO</span> - VISUAL</div>
  </div>
</body>
</html>
```